Bespoke catering company needs a simple but effective kick ass website

I need a website for a bespoke catering company based in the west side of Melbourne called "plova" by Marcus Feltham, I used the words Food-Dining-Events on my business cards which i still want to maintain through out the site.
My main market is aimed towards, in-house dining experiences of restaurant quality, cocktail food, small weddings / engagements, small events.
I have a plova logo in yellow in Hoefler title font with a black background, so the website design would include yellow and black and still using the Hoefler Titling font.
I want the site map to have 5 drop down bars including Home, About Me, Gallery, Menu, Contact me. It needs to be easy to move around.
I want links to my Facebook page, instagram and twitter.
The site needs to be easy for myself to change on a regular basis due to changing seasonal menus and gallery pictures.
Updates
Hi,
I have just added loads of photos of my food into the brief and adjusted the preferences slightly. Can you please update your submissions using my photos?
Thanks,
Marcus
Target Market(s)
The target market is customers looking for quality ,restaurant style dining and cocktail food in their own home or for their private event.
Industry/Entity Type
Restaurant
Font styles to use
Other font styles liked:
- Hoefler Titling
Look and feel
Each slider illustrates characteristics of the customer's brand and the style your logo design should communicate.

```html
<!DOCTYPE html>
<html lang="en">
<head>
<meta charset="utf-8">
<title>plova — by Marcus Feltham</title>
<link href="https://fonts.googleapis.com/css2?family=Lato:wght@400;700&display=swap" rel="stylesheet">
<style>
  :root {
    --ink: #2b2827;
    --ink-deep: #1f1d1c;
    --yellow-top: #ffea00;
    --yellow-bottom: #ffc600;
    --yellow-head: #ffd400;
    --white: #ffffff;
    --text-dark: #3a3000;
    --text-light: #f2f2f2;
  }
  * { box-sizing: border-box; margin: 0; padding: 0; }
  html, body { width: 1147px; height: 1200px; overflow: hidden; }
  body { font-family: "Lato", sans-serif; background: var(--ink); position: relative; }

  .top-bar { position: absolute; left: 0; top: 0; width: 1147px; height: 48px; background: var(--ink); }
  .search { position: absolute; left: 804px; top: 12px; width: 235px; height: 25px; background: var(--white); border: 1px solid #d8d8d8; border-radius: 2px; font-size: 9px; color: #9a9a9a; padding: 7px 8px; }
  .search svg { position: absolute; right: 6px; top: 5px; }

  .masthead { position: absolute; left: 0; top: 48px; width: 1147px; height: 89px; background: linear-gradient(var(--yellow-top), var(--yellow-bottom)); }
  .brand { position: absolute; left: 116px; top: 0; width: 148px; height: 89px; background: var(--ink-deep); color: var(--white); text-align: center; }
  .brand-name { font-size: 50px; font-weight: 400; line-height: 1; padding-top: 12px; letter-spacing: -1px; }
  .brand-by { position: absolute; right: 10px; bottom: 10px; font-size: 8px; color: var(--yellow-head); }

  .main-nav { position: absolute; top: 0; height: 89px; left: 0; width: 1147px; }
  .main-nav a { position: absolute; top: 37px; font-size: 16px; font-weight: 700; color: var(--white); text-decoration: none; }
  .main-nav a.is-current { color: var(--ink); }
  .nav-divider { position: absolute; top: 0; width: 1px; height: 89px; background: rgba(230,180,0,0.55); }

  .hero { position: absolute; left: 0; top: 137px; width: 1147px; height: 451px; background: radial-gradient(ellipse at 45% 40%, #d9b88a 0%, #b8905e 35%, #4a4660 75%, #2e2b44 100%); }
  .hero-arrow { position: absolute; top: 191px; }

  .highlights { position: absolute; left: 0; top: 588px; width: 1147px; height: 213px; background: linear-gradient(var(--yellow-top), var(--yellow-bottom)); }
  .highlight-photo { position: absolute; top: 29px; width: 287px; height: 145px; }
  .highlight-label { position: absolute; top: 184px; font-size: 14px; font-weight: 700; color: var(--text-dark); }

  .features { position: absolute; left: 0; top: 801px; width: 1147px; height: 308px; background: var(--ink); }
  .feature { position: absolute; top: 35px; width: 249px; }
  .feature h2 { font-size: 14px; font-weight: 700; color: var(--yellow-head); height: 24px; }
  .feature-photo { width: 248px; height: 123px; }
  .feature p { margin-top: 14px; font-size: 10px; line-height: 17.4px; color: var(--text-light); text-align: justify; }
  .gallery-photo { position: relative; width: 249px; height: 189px; background: linear-gradient(135deg, #b08a3c, #c9b070 45%, #8f9a4a 70%, #6c5028); }
  .gallery-photo svg { position: absolute; top: 76px; }

  .site-footer { position: absolute; left: 0; top: 1109px; width: 1147px; height: 91px; background: linear-gradient(var(--yellow-top), var(--yellow-bottom)); color: var(--text-dark); }
  .footer-nav { position: absolute; left: 122px; top: 22px; font-size: 12px; }
  .footer-nav a { color: var(--text-dark); text-decoration: none; }
  .footer-nav .sep { margin: 0 14px; }
  .copyright { position: absolute; left: 122px; top: 52px; font-size: 12px; }
  .social { position: absolute; top: 32px; width: 26px; height: 26px; border-radius: 50%; background: var(--white); border: 2px solid #f3d35a; }
</style>
</head>
<body>
  <header>
    <div class="top-bar">
      <div class="search">Type search
        <svg width="12" height="12" viewBox="0 0 12 12"><circle cx="5" cy="5" r="3.5" fill="none" stroke="#999" stroke-width="1.3"/><line x1="7.5" y1="7.5" x2="11" y2="11" stroke="#999" stroke-width="1.5"/></svg>
      </div>
    </div>
    <div class="masthead">
      <div class="brand"><div class="brand-name">plova</div><div class="brand-by">by marcus feltham</div></div>
      <nav class="main-nav">
        <a class="is-current" href="#" style="left:564px">HOME</a>
        <span class="nav-divider" style="left:600px"></span>
        <a href="#" style="left:645px">ABOUT ME</a>
        <span class="nav-divider" style="left:720px"></span>
        <a href="#" style="left:759px">GALLERY</a>
        <span class="nav-divider" style="left:813px"></span>
        <a href="#" style="left:857px">MENU</a>
        <span class="nav-divider" style="left:896px"></span>
        <a href="#" style="left:938px">CONTACT ME</a>
      </nav>
    </div>
  </header>

  <section class="hero" role="img" aria-label="Close-up of pastry tartlets topped with crumble, rolled cucumber ribbons and dill on a dark slate">
    <svg class="hero-arrow" style="left:59px" width="58" height="58" viewBox="0 0 58 58"><circle cx="29" cy="29" r="28" fill="#fff"/><polyline points="33,17 21,29 33,41" fill="none" stroke="#333" stroke-width="5" stroke-linecap="round" stroke-linejoin="round"/></svg>
    <svg class="hero-arrow" style="left:1034px" width="58" height="58" viewBox="0 0 58 58"><circle cx="29" cy="29" r="28" fill="#fff"/><polyline points="25,17 37,29 25,41" fill="none" stroke="#555" stroke-width="3" stroke-linecap="round" stroke-linejoin="round"/></svg>
  </section>

  <section class="highlights">
    <div class="highlight-photo" style="left:123px;background:linear-gradient(135deg,#d8cfc4,#b98a55 50%,#6e4a2a)" role="img" aria-label="Mini burgers on skewers arranged on a wooden board"></div>
    <div class="highlight-label" style="left:122px">Food</div>
    <div class="highlight-photo" style="left:431px;background:linear-gradient(135deg,#e8ece4,#9fb08a 50%,#6a4a30)" role="img" aria-label="White flower arrangement on a wooden event table"></div>
    <div class="highlight-label" style="left:431px">Events</div>
    <div class="highlight-photo" style="left:736px;background:linear-gradient(135deg,#4a5a58,#9a7a4a 50%,#2e2620)" role="img" aria-label="Guests at a candlelit dining table set with plates and glasses"></div>
    <div class="highlight-label" style="left:735px">Dinning</div>
  </section>

  <section class="features">
    <article class="feature" style="left:145px">
      <h2>About Me</h2>
      <div class="feature-photo" style="background:linear-gradient(90deg,#b01e3a,#3a3436 40%,#262424)" role="img" aria-label="Portrait of the chef in a black shirt in front of a neon sign"></div>
      <p>Lorem Ipsum is simply dummy text of the printing and typesetting industry. Lorem Ipsum has been the industry's standard dummy text ever since the 1500s, when an unknown printer took .</p>
    </article>
    <article class="feature" style="left:450px">
      <h2>Menu of the day</h2>
      <div class="feature-photo" style="background:linear-gradient(135deg,#cbb89a,#9a7a52 45%,#b0b060 70%,#d8cfc0)" role="img" aria-label="Cheese board with grapes, nuts and olives on a wooden table"></div>
      <p>Lorem Ipsum is simply dummy text of the printing and typesetting industry. Lorem Ipsum has been the industry's standard dummy text ever since the 1500s, when an unknown printer</p>
    </article>
    <article class="feature" style="left:755px">
      <h2>Gallery</h2>
      <div class="gallery-photo" role="img" aria-label="Dumplings with green garnish on skewers in a bamboo steamer">
        <svg style="left:12px" width="24" height="24" viewBox="0 0 24 24"><circle cx="12" cy="12" r="11" fill="#fff"/><polyline points="14,7 9,12 14,17" fill="none" stroke="#333" stroke-width="2.5" stroke-linecap="round" stroke-linejoin="round"/></svg>
        <svg style="left:221px" width="24" height="24" viewBox="0 0 24 24"><circle cx="12" cy="12" r="11" fill="#fff"/><polyline points="10,7 15,12 10,17" fill="none" stroke="#333" stroke-width="2.5" stroke-linecap="round" stroke-linejoin="round"/></svg>
      </div>
    </article>
  </section>

  <footer class="site-footer">
    <nav class="footer-nav">
      <a href="#">Home</a><span class="sep">|</span><a href="#">About Me</a><span class="sep">|</span><a href="#">Gallery</a><span class="sep">|</span><a href="#">Menu</a><span class="sep">|</span><a href="#">Contact me</a>
    </nav>
    <div class="copyright">Copyright ©2013 Company Name &nbsp;- All rights reserved</div>
    <a class="social" href="#" style="left:933px" aria-label="Social link one"></a>
    <a class="social" href="#" style="left:965px" aria-label="Social link two"></a>
    <a class="social" href="#" style="left:997px" aria-label="Social link three"></a>
  </footer>
</body>
</html>
```